Osteopath Advert Flyer for 20% discount

Osteopathic treatment services (much like the flyer design I found on google which brought me to your website - "Spinal Calm Bodywork"
I very much like the left side of that screenshot with the graphic design body rather than a real person.
If double sided, here are further details for what it is I do (this is optional if it is double sided). Ideally one side eye catching and the other with more information.
____________________________
Osteopathy can offer great results for those seeking immediate care with painful conditions and also for those wishing to invest in long-term health solutions. Treatments are tailored to the individual’s need, regardless of age or condition, my goal is to provide the best medical care whether it be treatment or more appropriate referral.

Osteopathy focuses on health promotion and disease prevention in order to help each person achieve a high level of wellness.

Osteopathy uses conventional medical assessment and techniques when gathering detail during diagnostic procedures. However, the real strength of osteopathy lies within the unique approach to which a patient and the condition are assessed and treated. Each patient is assessed from both a mechanical and functional viewpoint and treatment is based on these findings and patient requirements. Manual treatment methods are applied to suit the needs of the individual patient.

The overall goal is to achieve wellness by restoring balance and flexibility to the whole body.
_____________________________
I live in a small Island called Jersey and word-of-mouth is everything here. Therefore, I'd like a flyer that clearly indicates I treat people and aim to help people out of pain and injury but also give a very relaxing and enjoyable experience. So, not too clinical but also not to imaginary/idealistic massage room spa treatment.

Osteopathy is more or less in between a physio and a chiropractor (with regards to design style of this flyer). Of course it is somewhat very different to those professions, however, for this purpose the overall aim/style would be similar.

Please note: I do not particularly desire being on the flyer myself, however, it could be quite useful so I am happy for you to decide whether it may be of benefit.The aim is to attract the eye of the people walking past the flyer and to look professional but also interesting as many people will not have seen an osteopath before.

Thank you!

Target Market(s)

All humans above ages for 10

Industry/Entity Type

Healthcare

Font styles to use
Serif
Sans Serif

Colors
3377b5
33a6d7
ffffff
34a7d7
3277b5
85acd3
85cae6

Requirements
Must have
• 07416 352 704
contact@bvelintorask.co.uk
www.bvelintorask.co.uk

Tawny Brook Clinic
La Rue Des Pins
St Lawrence
Jersey
JE4 8QX

20% off with this flyer (*for initial consultation only*)
Nice to have
• Initial Consultation £55 for 45 minutes
Follow-Up Treatment £50 for 30 minutes

Treatment areas (much like in the flyers I attached as screenshots from google)
Headaches
Neck pain
Shoulder pain
Elbow and hand pain
Back pain
Hip pain
Knee pain
Ankle and foot pain
Arthritic pains
Chronic pain
Should not have
• No age range/indication of ages applicable as I wish to help and treat everyone (above the age of 10 for I do not specialise in paediatric osteopathy)

```html
<!DOCTYPE html>
<html lang="en">
<head>
<meta charset="utf-8">
<title>Spinal Calm Bodywork – Flyer</title>
<link rel="stylesheet" href="https://fonts.googleapis.com/css2?family=Open+Sans:wght@400;600;700&family=Roboto+Condensed:wght@400;700&display=swap">
<style>
  :root {
    --navy: #213a85;
    --navy-deep: #182c6b;
    --blue: #3377b5;
    --sky: #33a6d7;
    --soft: #85acd3;
    --pale: #85cae6;
    --white: #ffffff;
    --ink: #333a45;
    --stage: #e4e6e9;
  }
  * { box-sizing: border-box; margin: 0; padding: 0; }
  html, body { width: 1200px; height: 839px; overflow: hidden; }
  body { background: var(--stage); font-family: "Open Sans", Arial, sans-serif; position: relative; }

  .flyer {
    position: absolute; top: 73px; width: 464px; height: 657px;
    background: var(--white); overflow: hidden;
    box-shadow: 0 6px 18px rgba(0,0,0,.25);
  }
  .flyer--info { left: 92px; }
  .flyer--offer { left: 612px; }

  .photo { position: absolute; left: 0; top: 0; width: 464px; height: 290px; }
  .photo--back { background: linear-gradient(180deg, #6f8a63 0%, #4d6f86 40%, #365a8e 70%, #2e4b7c 100%); }
  .photo--neck { background: linear-gradient(115deg, #efece8 0%, #e2d9d1 45%, #d9c2bf 62%, #cfcac4 100%); }

  .overlay { position: absolute; left: 0; top: 0; }

  .brand { position: absolute; left: 16px; top: 20px; display: flex; align-items: center; gap: 6px; }
  .brand__dot { width: 10px; height: 10px; border-radius: 50%; background: var(--sky); }
  .brand__name { font: 600 13px "Open Sans", Arial, sans-serif; color: var(--blue); }

  .title {
    position: absolute; left: 14px; top: 279px;
    font: 700 19px/24px "Roboto Condensed", Arial Narrow, sans-serif; color: var(--navy); letter-spacing: .2px;
  }
  .intro {
    position: absolute; left: 14px; top: 305px; width: 320px;
    font-size: 8.2px; line-height: 1.3; color: var(--ink); text-align: justify;
  }
  .highlight {
    position: absolute; left: 13px; top: 374px; width: 310px; height: 36px;
    background: linear-gradient(180deg, #2f63b3, var(--navy)); border-radius: 4px;
    box-shadow: 0 2px 4px rgba(0,0,0,.3), inset 0 0 0 1px rgba(255,255,255,.35);
    color: var(--white); font-weight: 700; font-size: 8.2px; line-height: 1.3;
    display: flex; align-items: center; justify-content: center; text-align: center; padding: 0 10px;
  }
  .benefits__title {
    position: absolute; left: 14px; top: 419px;
    font: 700 12.5px "Roboto Condensed", Arial Narrow, sans-serif; color: var(--navy);
  }
  .benefits { position: absolute; left: 14px; top: 438px; width: 316px; display: grid; grid-template-columns: 152px 152px; gap: 6px 12px; }
  .benefit__name { display: flex; align-items: center; gap: 4px; font: 600 8px "Open Sans", Arial, sans-serif; color: var(--blue); }
  .benefit__text { font-size: 6.9px; line-height: 1.22; color: #444; padding-left: 13px; margin-top: 1px; }

  .chev { width: 9px; height: 9px; flex: none; }

  .spot {
    position: absolute; left: 342px; width: 100px; height: 100px; border-radius: 50%;
    border: 3px solid var(--white); box-shadow: 0 0 0 2px var(--soft), 0 3px 6px rgba(0,0,0,.3);
  }
  .spot--shoulder { top: 258px; background: radial-gradient(circle at 40% 30%, #f06b55 0, #8d4a86 22%, #23479a 55%, #0f2460 100%); }
  .spot--knee { top: 360px; background: radial-gradient(circle at 55% 45%, #f4a24a 0, #d9573d 18%, #304e9d 55%, #12286a 100%); }
  .spot--wrist { top: 452px; background: radial-gradient(circle at 45% 45%, #f38a4a 0, #b4473f 20%, #294a98 55%, #10255f 100%); }
  .spot--hand { top: 548px; background: radial-gradient(circle at 50% 55%, #f07a45 0, #a8443c 22%, #2a4d9c 55%, #0f2360 100%); }

  .contact { position: absolute; left: 14px; top: 566px; color: var(--white); }
  .contact__title { font: 700 18px/22px "Roboto Condensed", Arial Narrow, sans-serif; margin-bottom: 3px; }
  .contact__line { display: flex; align-items: center; gap: 5px; font-size: 8.4px; line-height: 14.5px; }
  .contact__icon { width: 9px; height: 9px; flex: none; }

  /* Offer side */
  .ribbon { position: absolute; right: 0; top: 0; }
  .portrait {
    position: absolute; left: 316px; top: 232px; width: 140px; height: 140px; border-radius: 50%;
    border: 4px solid var(--white); box-shadow: 0 0 0 4px var(--blue), 0 3px 8px rgba(0,0,0,.3);
    background: linear-gradient(180deg, #e9ecef 0%, #d7dde3 55%, #c9d1d9 100%); overflow: hidden;
  }
  .portrait__label {
    position: absolute; left: 0; right: 0; bottom: 0; height: 34px; background: var(--navy);
    color: var(--white); text-align: center; font: 700 6.6px/1.25 "Roboto Condensed", Arial Narrow, sans-serif;
    padding-top: 6px;
  }
  .tab { position: absolute; left: 0; top: 307px; }
  .tab__text {
    position: absolute; left: 14px; top: 307px; line-height: 30px;
    font: 700 14.5px/30px "Roboto Condensed", Arial Narrow, sans-serif; color: var(--white); letter-spacing: .3px;
  }
  .treatments { position: absolute; left: 24px; top: 344px; width: 300px; display: grid; grid-template-columns: 166px 134px; grid-auto-rows: 24.3px; list-style: none; }
  .treatment { display: flex; align-items: center; gap: 9px; font: 400 12.5px "Roboto Condensed", Arial Narrow, sans-serif; color: var(--blue); white-space: nowrap; }

  .price {
    position: absolute; top: 473px; width: 152px; height: 62px; border-radius: 8px;
    background: linear-gradient(180deg, #2f64b4 0%, var(--navy) 100%);
    border: 2px solid var(--white); box-shadow: 0 0 0 1px var(--soft), 0 3px 7px rgba(0,0,0,.35);
    color: var(--white); display: flex; align-items: center; gap: 5px; padding-left: 8px;
  }
  .price--initial { left: 24px; }
  .price--follow { left: 196px; }
  .price__amount { font: 700 36px/1 "Roboto Condensed", Arial Narrow, sans-serif; letter-spacing: -1px; }
  .price__label { font: 700 9.5px/1.1 "Roboto Condensed", Arial Narrow, sans-serif; }
  .price__time { display: block; font: 400 7.5px "Open Sans", Arial, sans-serif; margin-top: 2px; }
</style>
</head>
<body>

<!-- Information side -->
<article class="flyer flyer--info">
  <div class="photo photo--back" role="img" aria-label="Photo of a man holding his lower back with a glowing spine overlay"></div>

  <svg class="overlay" width="464" height="300" viewBox="0 0 464 300" aria-hidden="true">
    <path d="M0,0 L290,0 C225,35 130,70 0,110 Z" fill="#ffffff"/>
    <path d="M290,0 C225,35 130,70 0,110" fill="none" stroke="#3377b5" stroke-width="5"/>
    <path d="M276,0 C214,32 122,64 0,100" fill="none" stroke="#85acd3" stroke-width="2"/>
    <path d="M0,165 C110,215 240,262 464,268 L464,300 L0,300 Z" fill="#ffffff"/>
    <path d="M0,158 C110,208 240,255 464,261" fill="none" stroke="#213a85" stroke-width="6"/>
    <path d="M0,170 C110,220 240,266 464,272" fill="none" stroke="#85acd3" stroke-width="2"/>
  </svg>

  <div class="brand"><span class="brand__dot"></span><span class="brand__name">Bram Velintorask</span></div>

  <h1 class="title">SPINAL CALM BODYWORK</h1>
  <p class="intro">Osteopathy can offer great results for those seeking immediate care with painful conditions and also for those wishing to invest in long-term health solutions. Treatments are tailored to the individual’s need, regardless of age or condition, my goal is to provide the best medical care whether it be treatment or more appropriate referral.</p>
  <div class="highlight">Osteopathy focuses on health promotion and disease prevention in order to help each person achieve a high level of wellness.</div>

  <h2 class="benefits__title">THE BENEFITS OF OSTEOPATHY</h2>
  <div class="benefits">
    <div class="benefit">
      <div class="benefit__name"><svg class="chev" viewBox="0 0 10 10"><circle cx="5" cy="5" r="5" fill="#3377b5"/><path d="M4,2.8 L6.2,5 L4,7.2" fill="none" stroke="#fff" stroke-width="1.3"/></svg>Manage Chronic Pain</div>
      <p class="benefit__text">Restores musculoskeletal system, underlying tissues, including organs, as well.</p>
    </div>
    <div class="benefit">
      <div class="benefit__name"><svg class="chev" viewBox="0 0 10 10"><circle cx="5" cy="5" r="5" fill="#3377b5"/><path d="M4,2.8 L6.2,5 L4,7.2" fill="none" stroke="#fff" stroke-width="1.3"/></svg>Promote Fluid Flow</div>
      <p class="benefit__text">Increase circulation into the body, reduce blood pressure, decrease inflammation and bodily detox.</p>
    </div>
    <div class="benefit">
      <div class="benefit__name"><svg class="chev" viewBox="0 0 10 10"><circle cx="5" cy="5" r="5" fill="#3377b5"/><path d="M4,2.8 L6.2,5 L4,7.2" fill="none" stroke="#fff" stroke-width="1.3"/></svg>Prevent Injury</div>
      <p class="benefit__text">Osteopathic treatments increase muscular flexion and resilience, thereby increasing range of motion and preventing tearing.</p>
    </div>
    <div class="benefit">
      <div class="benefit__name"><svg class="chev" viewBox="0 0 10 10"><circle cx="5" cy="5" r="5" fill="#3377b5"/><path d="M4,2.8 L6.2,5 L4,7.2" fill="none" stroke="#fff" stroke-width="1.3"/></svg>Aid Relaxation</div>
      <p class="benefit__text">Increase dopamine levels, and promote relaxation and wellness. Improving circulation, lymphatic flow, and vascular response.</p>
    </div>
  </div>

  <svg class="overlay" style="top:530px" width="464" height="127" viewBox="0 0 464 127" aria-hidden="true">
    <path d="M0,16 C150,6 300,28 464,86 L464,127 L0,127 Z" fill="#85cae6"/>
    <path d="M0,24 C150,14 300,36 464,94 L464,127 L0,127 Z" fill="#213a85"/>
  </svg>

  <div class="spot spot--shoulder" role="img" aria-label="Illustration of a highlighted shoulder joint"></div>
  <div class="spot spot--knee" role="img" aria-label="Illustration of a highlighted knee joint"></div>
  <div class="spot spot--wrist" role="img" aria-label="Illustration of a highlighted wrist and hand"></div>
  <div class="spot spot--hand" role="img" aria-label="Illustration of a highlighted forearm and hand"></div>

  <div class="contact">
    <div class="contact__title">CONTACT US:</div>
    <div class="contact__line"><svg class="contact__icon" viewBox="0 0 10 10"><circle cx="5" cy="5" r="5" fill="#85cae6"/><path d="M3.2,2.6 L4.2,2.6 L4.6,3.9 L4,4.4 C4.4,5.3 4.8,5.7 5.6,6 L6.1,5.4 L7.4,5.8 L7.4,6.8 C5,7 3,5 3.2,2.6Z" fill="#213a85"/></svg>07416 352 704</div>
    <div class="contact__line"><svg class="contact__icon" viewBox="0 0 10 10"><circle cx="5" cy="5" r="5" fill="#85cae6"/><rect x="2.6" y="3.3" width="4.8" height="3.4" fill="#213a85"/><path d="M2.6,3.3 L5,5.2 L7.4,3.3" fill="none" stroke="#85cae6" stroke-width=".6"/></svg>contact@bvelintorask.co.uk</div>
    <div class="contact__line"><svg class="contact__icon" viewBox="0 0 10 10"><circle cx="5" cy="5" r="5" fill="#85cae6"/><circle cx="5" cy="5" r="2.5" fill="none" stroke="#213a85" stroke-width=".8"/><path d="M2.5,5 H7.5 M5,2.5 V7.5" stroke="#213a85" stroke-width=".6"/></svg>www.bvelintorask.co.uk</div>
    <div class="contact__line"><svg class="contact__icon" viewBox="0 0 10 10"><circle cx="5" cy="5" r="5" fill="#85cae6"/><path d="M5,8 C3.5,6 3,5 3,4.1 A2,2 0 0 1 7,4.1 C7,5 6.5,6 5,8Z" fill="#213a85"/><circle cx="5" cy="4.1" r=".8" fill="#85cae6"/></svg>La Rue Des Pins St Lawrence Jersey JE4 8QX</div>
  </div>
</article>

<!-- Offer side -->
<article class="flyer flyer--offer">
  <div class="photo photo--neck" role="img" aria-label="Photo of a woman on a sofa holding her sore neck"></div>

  <svg class="overlay" width="464" height="460" viewBox="0 0 464 460" aria-hidden="true">
    <path d="M0,0 L290,0 C225,35 130,70 0,110 Z" fill="#ffffff"/>
    <path d="M290,0 C225,35 130,70 0,110" fill="none" stroke="#3377b5" stroke-width="5"/>
    <path d="M276,0 C214,32 122,64 0,100" fill="none" stroke="#85acd3" stroke-width="2"/>
    <path d="M0,200 C30,160 60,170 110,205 C170,248 240,266 320,270 L464,272 L464,460 L0,460 Z" fill="#ffffff"/>
    <path d="M0,192 C30,152 62,162 112,197 C170,240 240,258 320,262" fill="none" stroke="#3377b5" stroke-width="5"/>
    <path d="M0,204 C30,166 62,176 112,210" fill="none" stroke="#85acd3" stroke-width="2"/>
    <path d="M380,392 C415,400 440,410 464,424 L464,452 C440,436 415,414 380,400 Z" fill="#213a85"/>
    <path d="M380,378 C415,386 440,394 464,404 L464,414 C440,404 415,394 380,386 Z" fill="#33a6d7"/>
  </svg>

  <svg class="ribbon" width="122" height="100" viewBox="0 0 122 100" aria-hidden="true">
    <polygon points="0,0 122,0 122,100" fill="#213a85"/>
    <g transform="translate(80,34) rotate(39)" fill="#ffffff" text-anchor="middle" font-family="'Roboto Condensed', Arial Narrow, sans-serif">
      <text y="-6" font-size="12" font-weight="700">20% OFF</text>
      <text y="6" font-size="10" font-weight="700">WITH THIS FLYER</text>
      <text y="15" font-size="6">(*for initial consultation only)</text>
    </g>
  </svg>

  <div class="brand"><span class="brand__dot"></span><span class="brand__name">Bram Velintorask</span></div>

  <div class="portrait" role="img" aria-label="Portrait photo of the osteopath in a white clinic tunic">
    <div class="portrait__label">BRAM VELINTORASK<br>OSTEOPATH &amp; NATUROPATH</div>
  </div>

  <h1 class="title">SPINAL CALM BODYWORK</h1>

  <svg class="tab" width="282" height="30" viewBox="0 0 282 30" aria-hidden="true">
    <polygon points="0,0 268,0 282,30 0,30" fill="#213a85"/>
  </svg>
  <div class="tab__text">OUR TREATMENTS</div>

  <ul class="treatments">
    <li class="treatment"><svg class="chev" viewBox="0 0 10 10"><circle cx="5" cy="5" r="5" fill="#3377b5"/><path d="M4,2.8 L6.2,5 L4,7.2" fill="none" stroke="#fff" stroke-width="1.3"/></svg>HEADACHES</li>
    <li class="treatment"><svg class="chev" viewBox="0 0 10 10"><circle cx="5" cy="5" r="5" fill="#3377b5"/><path d="M4,2.8 L6.2,5 L4,7.2" fill="none" stroke="#fff" stroke-width="1.3"/></svg>HIP PAIN</li>
    <li class="treatment"><svg class="chev" viewBox="0 0 10 10"><circle cx="5" cy="5" r="5" fill="#3377b5"/><path d="M4,2.8 L6.2,5 L4,7.2" fill="none" stroke="#fff" stroke-width="1.3"/></svg>NECK PAIN</li>
    <li class="treatment"><svg class="chev" viewBox="0 0 10 10"><circle cx="5" cy="5" r="5" fill="#3377b5"/><path d="M4,2.8 L6.2,5 L4,7.2" fill="none" stroke="#fff" stroke-width="1.3"/></svg>KNEE PAIN</li>
    <li class="treatment"><svg class="chev" viewBox="0 0 10 10"><circle cx="5" cy="5" r="5" fill="#3377b5"/><path d="M4,2.8 L6.2,5 L4,7.2" fill="none" stroke="#fff" stroke-width="1.3"/></svg>SHOULDER PAIN</li>
    <li class="treatment"><svg class="chev" viewBox="0 0 10 10"><circle cx="5" cy="5" r="5" fill="#3377b5"/><path d="M4,2.8 L6.2,5 L4,7.2" fill="none" stroke="#fff" stroke-width="1.3"/></svg>ANKLE AND FOOT PAIN</li>
    <li class="treatment"><svg class="chev" viewBox="0 0 10 10"><circle cx="5" cy="5" r="5" fill="#3377b5"/><path d="M4,2.8 L6.2,5 L4,7.2" fill="none" stroke="#fff" stroke-width="1.3"/></svg>ELBOW AND HAND PAIN</li>
    <li class="treatment"><svg class="chev" viewBox="0 0 10 10"><circle cx="5" cy="5" r="5" fill="#3377b5"/><path d="M4,2.8 L6.2,5 L4,7.2" fill="none" stroke="#fff" stroke-width="1.3"/></svg>ARTHRITIC PAINS</li>
    <li class="treatment"><svg class="chev" viewBox="0 0 10 10"><circle cx="5" cy="5" r="5" fill="#3377b5"/><path d="M4,2.8 L6.2,5 L4,7.2" fill="none" stroke="#fff" stroke-width="1.3"/></svg>BACK PAIN</li>
    <li class="treatment"><svg class="chev" viewBox="0 0 10 10"><circle cx="5" cy="5" r="5" fill="#3377b5"/><path d="M4,2.8 L6.2,5 L4,7.2" fill="none" stroke="#fff" stroke-width="1.3"/></svg>CHRONIC PAIN</li>
  </ul>

  <svg class="overlay" style="top:530px" width="464" height="127" viewBox="0 0 464 127">
    <defs>
      <linearGradient id="xrayTone" x1="0" y1="0" x2="1" y2="1">
        <stop offset="0" stop-color="#33a6d7"/>
        <stop offset=".6" stop-color="#1f5fad"/>
        <stop offset="1" stop-color="#182c6b"/>
      </linearGradient>
    </defs>
    <path d="M262,22 C330,0 400,6 464,0 L464,127 L262,127 Z" fill="url(#xrayTone)" role="img" aria-label="Illustration of a lower spine with a highlighted pain point"/>
    <path d="M0,16 C120,6 230,28 310,78 C336,96 352,114 362,127 L0,127 Z" fill="#85cae6" aria-hidden="true"/>
    <path d="M0,24 C120,14 222,36 298,86 C322,102 336,118 344,127 L0,127 Z" fill="#213a85" aria-hidden="true"/>
  </svg>

  <div class="price price--initial">
    <span class="price__amount">£55</span>
    <span class="price__label">INITIAL<br>CONSULTATION<span class="price__time">for 45 minutes</span></span>
  </div>
  <div class="price price--follow">
    <span class="price__amount">£50</span>
    <span class="price__label">FOLLOW-UP<br>TREATMENT<span class="price__time">for 30 minutes</span></span>
  </div>

  <div class="contact">
    <div class="contact__title">CONTACT US:</div>
    <div class="contact__line"><svg class="contact__icon" viewBox="0 0 10 10"><circle cx="5" cy="5" r="5" fill="#85cae6"/><path d="M3.2,2.6 L4.2,2.6 L4.6,3.9 L4,4.4 C4.4,5.3 4.8,5.7 5.6,6 L6.1,5.4 L7.4,5.8 L7.4,6.8 C5,7 3,5 3.2,2.6Z" fill="#213a85"/></svg>07416 352 704</div>
    <div class="contact__line"><svg class="contact__icon" viewBox="0 0 10 10"><circle cx="5" cy="5" r="5" fill="#85cae6"/><rect x="2.6" y="3.3" width="4.8" height="3.4" fill="#213a85"/><path d="M2.6,3.3 L5,5.2 L7.4,3.3" fill="none" stroke="#85cae6" stroke-width=".6"/></svg>contact@bvelintorask.co.uk</div>
    <div class="contact__line"><svg class="contact__icon" viewBox="0 0 10 10"><circle cx="5" cy="5" r="5" fill="#85cae6"/><circle cx="5" cy="5" r="2.5" fill="none" stroke="#213a85" stroke-width=".8"/><path d="M2.5,5 H7.5 M5,2.5 V7.5" stroke="#213a85" stroke-width=".6"/></svg>www.bvelintorask.co.uk</div>
    <div class="contact__line"><svg class="contact__icon" viewBox="0 0 10 10"><circle cx="5" cy="5" r="5" fill="#85cae6"/><path d="M5,8 C3.5,6 3,5 3,4.1 A2,2 0 0 1 7,4.1 C7,5 6.5,6 5,8Z" fill="#213a85"/><circle cx="5" cy="4.1" r=".8" fill="#85cae6"/></svg>La Rue Des Pins St Lawrence Jersey JE4 8QX</div>
  </div>
</article>

</body>
</html>
```